Brivolt VoIP COMMERCIAL PHONE FLYER

We are a full service telecom VoIP company that offers local, long distance calling plans to business clients. We offer local installations, and local service we have a hands on approach and will match or beat any competitor. We work with all types of business. We are fully HIPPA complient in the medical field

Target Market(s)

SMALL TO MEDIUM BUSINESS, Medical, Real Estate, Lawyer, Accounting

Industry/Entity Type

VoIP

Font styles to use
Serif

Colors
0054AA
0677BA
7BADD7
CADEEF
E8F1F8

Requirements
Must have
• Modern/ Current picture of phone reader friendly
Nice to have
• free flow, friendly, modern
Should not have
• stuffy, corporate feel

```html
<!DOCTYPE html>
<html lang="en">
<head>
<meta charset="utf-8">
<title>Brivolt VoIP Flyer</title>
<link rel="stylesheet" href="https://fonts.googleapis.com/css2?family=Montserrat:wght@300;400;600;700;800&family=Oswald:wght@700&display=swap">
<style>
  :root {
    --navy: #0a3470;
    --navy-deep: #062555;
    --blue: #0054aa;
    --blue-bright: #0677ba;
    --blue-soft: #7badd7;
    --blue-pale: #cadeef;
    --blue-mist: #e8f1f8;
    --ink: #1c1c1c;
    --grey: #6b6b6b;
    --white: #ffffff;
  }
  * { margin: 0; padding: 0; box-sizing: border-box; }
  html, body { width: 783px; height: 1200px; overflow: hidden; background: var(--white); }
  .flyer {
    position: relative; width: 783px; height: 1200px; overflow: hidden;
    font-family: "Montserrat", sans-serif; color: var(--ink); background: var(--white);
  }
  .hero-shape { position: absolute; inset: 0; width: 783px; height: 1200px; }
  .brand {
    position: absolute; top: 62px; left: 0; width: 100%;
    display: flex; justify-content: center; align-items: center; gap: 12px;
    color: var(--white); font-weight: 700; font-size: 44px; letter-spacing: 2px;
  }
  .brand-dot { width: 18px; height: 18px; border-radius: 50%; background: var(--white); }
  .headline { position: absolute; top: 148px; left: 0; width: 100%; text-align: center; color: var(--white); }
  .headline .lead { font-weight: 300; font-size: 46px; letter-spacing: 1px; line-height: 54px; }
  .headline .main { font-weight: 800; font-size: 53px; letter-spacing: 1px; line-height: 58px; }
  .headline .tail { font-weight: 400; font-size: 36px; letter-spacing: 1px; line-height: 48px; }
  .rule { position: absolute; top: 332px; left: 240px; width: 300px; height: 1px; background: var(--blue-soft); }
  .rule::after { content: ""; position: absolute; left: 130px; top: -2px; width: 40px; height: 5px; border-radius: 3px; background: var(--white); }
  .phone-photo {
    position: absolute; left: 48px; top: 340px; width: 540px; height: 420px;
    border-radius: 28px 28px 40px 60px;
    background: linear-gradient(150deg, #5a5e66 0%, #2b2e33 45%, #15171a 100%);
  }
  .cloud-badge {
    position: absolute; left: 548px; top: 552px; width: 192px; height: 192px; border-radius: 50%;
    background: radial-gradient(circle at 40% 35%, var(--blue-bright), var(--blue) 70%, #003d80);
    display: flex; flex-direction: column; align-items: center; justify-content: center;
    color: var(--white); text-align: center;
  }
  .cloud-badge::before { content: ""; position: absolute; inset: 12px; border-radius: 50%; border: 2px dashed var(--white); }
  .cloud-badge .small { font-weight: 400; font-size: 17px; }
  .cloud-badge .big { font-weight: 700; font-size: 23px; line-height: 29px; }
  .savings { position: absolute; left: 76px; top: 770px; }
  .savings .intro { font-weight: 700; font-size: 24px; }
  .savings .amount { font-weight: 800; font-size: 55px; letter-spacing: 1px; line-height: 58px; }
  .savings .detail { font-weight: 700; font-size: 23.5px; }
  .savings-divider { position: absolute; left: 476px; top: 790px; height: 100px; border-left: 2px dotted #999; }
  .percent {
    position: absolute; left: 498px; top: 760px;
    font-family: "Oswald", sans-serif; font-weight: 700; font-size: 122px; line-height: 140px;
    color: var(--blue-bright); letter-spacing: -2px;
  }
  .features {
    position: absolute; left: 59px; top: 935px; width: 666px; height: 135px;
    border: 2px solid var(--ink); border-radius: 14px;
    display: flex; align-items: center;
  }
  .feature { flex: 1; display: flex; flex-direction: column; align-items: center; gap: 10px; position: relative; }
  .feature + .feature::before { content: ""; position: absolute; left: 0; top: 6px; height: 92px; border-left: 2px solid #bbb; }
  .feature-icon { width: 80px; height: 80px; }
  .feature-label { font-weight: 700; font-size: 18px; }
  .footer-contacts {
    position: absolute; left: 60px; top: 1134px; display: flex; gap: 18px; align-items: center;
    color: var(--white); font-weight: 700;
  }
  .contact { display: flex; align-items: center; gap: 6px; }
  .contact.phone { font-size: 21px; }
  .contact.mail { font-size: 16px; }
  .web { position: absolute; left: 568px; top: 1140px; font-weight: 700; font-size: 16px; color: var(--ink); }
</style>
</head>
<body>
<div class="flyer">
  <svg class="hero-shape" viewBox="0 0 783 1200" aria-hidden="true">
    <defs>
      <radialGradient id="heroGlow" cx="50%" cy="30%" r="65%">
        <stop offset="0" stop-color="#1a5cae"/>
        <stop offset="0.6" stop-color="#0a3a7c"/>
        <stop offset="1" stop-color="#062555"/>
      </radialGradient>
      <linearGradient id="footerBand" x1="0" x2="1">
        <stop offset="0" stop-color="#062555"/>
        <stop offset="1" stop-color="#0b3f86"/>
      </linearGradient>
    </defs>
    <path d="M0 380 C30 380 40 420 75 410 C110 400 120 440 160 430 L160 320 L783 320 L783 210 C770 310 720 400 640 420 C610 430 600 470 560 470 L0 470 Z" fill="#6e6e6e"/>
    <path d="M0 0 H783 V195 C770 290 720 370 640 395 C600 405 590 440 550 445 C500 450 480 420 430 430 L160 430 C130 420 110 380 75 392 C45 402 30 360 0 362 Z" fill="url(#heroGlow)"/>
    <g stroke="#ffffff" stroke-opacity="0.05" stroke-width="40">
      <line x1="391" y1="230" x2="0" y2="0"/><line x1="391" y1="230" x2="200" y2="0"/>
      <line x1="391" y1="230" x2="580" y2="0"/><line x1="391" y1="230" x2="783" y2="0"/>
      <line x1="391" y1="230" x2="783" y2="200"/><line x1="391" y1="230" x2="0" y2="200"/>
    </g>
    <path d="M0 1107 H440 C480 1107 500 1130 530 1170 C550 1195 580 1196 620 1196 H783 V1200 H0 Z" fill="#7a7a7a"/>
    <path d="M0 1110 H420 C470 1110 495 1140 520 1170 C540 1192 570 1195 600 1195 L783 1195 V1200 H0 Z" fill="url(#footerBand)"/>
  </svg>

  <div class="brand"><span class="brand-dot"></span><span>Brivolt</span></div>

  <div class="headline">
    <div class="lead">WE OFFER FREE</div>
    <div class="main">TELEPHONE LINES</div>
    <div class="tail">FOR YOUR BUSINESS</div>
  </div>
  <div class="rule"></div>

  <div class="phone-photo" role="img" aria-label="Photo of a modern touchscreen desk phone with corded HD handset showing a video call"></div>

  <div class="cloud-badge">
    <span class="small">Your business</span>
    <span class="big">on the<br>cloud</span>
  </div>

  <div class="savings">
    <div class="intro">We help companies</div>
    <div class="amount">SAVE OVER</div>
    <div class="detail">On their monthly phone bills</div>
  </div>
  <div class="savings-divider"></div>
  <div class="percent">35%</div>

  <div class="features">
    <div class="feature">
      <svg class="feature-icon" viewBox="0 0 80 80" aria-hidden="true">
        <circle cx="40" cy="40" r="37" fill="none" stroke="#555" stroke-width="1.5" stroke-dasharray="2 3"/>
        <circle cx="40" cy="40" r="32" fill="none" stroke="#0677ba" stroke-width="5"/>
        <path d="M40 24a11 11 0 0 0-6 20v5h12v-5a11 11 0 0 0-6-20z" fill="none" stroke="#222" stroke-width="2"/>
        <line x1="35" y1="53" x2="45" y2="53" stroke="#222" stroke-width="2"/>
        <line x1="37" y1="57" x2="43" y2="57" stroke="#222" stroke-width="2"/>
      </svg>
      <span class="feature-label">Powerful features</span>
    </div>
    <div class="feature">
      <svg class="feature-icon" viewBox="0 0 80 80" aria-hidden="true">
        <circle cx="40" cy="40" r="37" fill="none" stroke="#555" stroke-width="1.5" stroke-dasharray="2 3"/>
        <circle cx="40" cy="40" r="32" fill="none" stroke="#0677ba" stroke-width="5"/>
        <ellipse cx="35" cy="36" rx="12" ry="9" fill="#222"/>
        <path d="M28 43 l-4 6 8-3z" fill="#222"/>
        <ellipse cx="47" cy="44" rx="9" ry="7" fill="#fff" stroke="#222" stroke-width="2"/>
        <path d="M52 49 l4 5-7-2z" fill="#222"/>
      </svg>
      <span class="feature-label">Easy to use</span>
    </div>
    <div class="feature">
      <svg class="feature-icon" viewBox="0 0 80 80" aria-hidden="true">
        <circle cx="40" cy="40" r="37" fill="none" stroke="#555" stroke-width="1.5" stroke-dasharray="2 3"/>
        <circle cx="40" cy="40" r="32" fill="none" stroke="#0677ba" stroke-width="5"/>
        <line x1="28" y1="52" x2="50" y2="30" stroke="#222" stroke-width="4" stroke-linecap="round"/>
        <circle cx="51" cy="29" r="5" fill="none" stroke="#222" stroke-width="2.5"/>
        <line x1="30" y1="28" x2="52" y2="50" stroke="#222" stroke-width="4" stroke-linecap="round"/>
        <rect x="25" y="23" width="9" height="7" transform="rotate(45 29 26)" fill="#222"/>
      </svg>
      <span class="feature-label">Easy set up</span>
    </div>
  </div>

  <div class="footer-contacts">
    <span class="contact phone">
      <svg width="18" height="18" viewBox="0 0 24 24" aria-hidden="true"><path d="M6.6 10.8a15 15 0 0 0 6.6 6.6l2.2-2.2a1 1 0 0 1 1-.25 11.4 11.4 0 0 0 3.6.57 1 1 0 0 1 1 1V20a1 1 0 0 1-1 1A17 17 0 0 1 3 4a1 1 0 0 1 1-1h3.5a1 1 0 0 1 1 1 11.4 11.4 0 0 0 .57 3.6 1 1 0 0 1-.25 1z" fill="#fff"/></svg>
      555.014.2290
    </span>
    <span class="contact mail">
      <svg width="18" height="13" viewBox="0 0 18 13" aria-hidden="true"><rect x="1" y="1" width="16" height="11" fill="none" stroke="#fff" stroke-width="1.5"/><path d="M1 1l8 6 8-6" fill="none" stroke="#fff" stroke-width="1.5"/></svg>
      hello@brivolt-voip.com
    </span>
  </div>
  <div class="web">www.brivolt-voip.com</div>
</div>
</body>
</html>
```